Boutique Store Selling Antiques and Unique Finds

I need a Web Page designed for my Store Called "Larkmoor Lane". I would like a very classic, muted design that looks European when pulled up. I will be selling Antiques from all over the world and Unique finds that have reproduced. I will also be selling high-end purses and jewelry with unique, reasonable products for the every-day buyer as well.

Target Market(s)

25-70 year old men and women;)

Coding

Coded - Design and coding required

Number of Pages Required

1 page

Colors

Designer to choose only greyscale colors for use in the design.

Requirements
Must have
• I want it

```html
<!DOCTYPE html>
<html lang="en">
<head>
<meta charset="utf-8">
<title>Larkmoor Lane — Antiques &amp; Unique Finds</title>
<link href="https://fonts.googleapis.com/css2?family=Lora:wght@400;500;600&family=Poppins:wght@400;500&display=swap" rel="stylesheet">
<style>
:root{
  --ink:#1c1b1d;
  --ink-deep:#131214;
  --text:#333333;
  --muted:#666666;
  --line:#d4d4d4;
  --paper:#ffffff;
  --mist:#f4f4f4;
  --white:#ffffff;
  --serif:'Lora', Georgia, serif;
  --sans:Arial, Helvetica, sans-serif;
  --round:'Poppins', Arial, sans-serif;
}
*{margin:0;padding:0;box-sizing:border-box}
html,body{width:1200px;height:3764px;overflow:hidden}
body{position:relative;background:var(--paper);font-family:var(--serif);color:var(--text)}
.abs{position:absolute}

/* top bar */
.topbar{left:0;top:0;width:1200px;height:53px;background:var(--ink);color:var(--white);font-size:14px}
.topbar .call{left:111px;top:17px}
.topbar .account{right:118px;top:17px;display:flex;align-items:center;gap:18px}
.topbar .account span.sep{opacity:.8}
.topbar svg{display:block}

/* header */
.brand{left:0;top:88px;width:1200px;text-align:center;font-family:var(--serif);font-size:28px;letter-spacing:5px;color:var(--ink);font-weight:500}
.header-rule{left:111px;top:165px;width:978px;height:1px;background:var(--line)}
.nav{top:188px;font-size:14px;text-transform:uppercase;color:var(--text);transform:translateX(-50%)}

/* hero */
.hero{left:0;top:231px;width:1200px;height:699px;background:radial-gradient(ellipse at 55% 55%,#5a4e43 0%,#3a322b 40%,#1f1a16 100%)}
.hero-title{left:0;top:550px;width:1200px;text-align:center;color:var(--white);font-size:54px;letter-spacing:9px;font-weight:500}
.hero-sub{left:0;top:638px;width:1200px;text-align:center;color:var(--white);font-size:18px;font-weight:600;letter-spacing:.3px}
.hero-btn{left:504px;top:687px;width:192px;height:61px;border:2px solid var(--white);border-radius:31px;color:var(--white);font-size:18px;font-weight:600;display:flex;align-items:center;justify-content:center}

/* section titles */
.section-title{left:0;width:1200px;text-align:center;font-size:38px;color:var(--ink);font-weight:400}
.title-rule{left:580px;width:40px;height:2px;background:var(--ink)}

/* products */
.product{width:231px;height:358px;background:var(--paper);box-shadow:0 0 6px rgba(0,0,0,.14)}
.product .photo{position:absolute;left:7px;top:9px;width:217px;height:184px}
.product .price{position:absolute;top:220px;width:100%;text-align:center;font-size:20px;color:var(--ink)}
.product .name{position:absolute;top:254px;width:100%;text-align:center;font-size:17px;color:var(--text)}
.product .details{position:absolute;left:47px;top:292px;width:137px;height:42px;border:1px solid #9a9a9a;border-radius:21px;display:flex;align-items:center;justify-content:center;font-size:15px;color:var(--text)}

/* feature */
.feature{left:0;top:1900px;width:1200px;height:478px;background:linear-gradient(90deg,#cdbfae 0%,#d9cdbf 50%,#d6cabb 100%)}
.feature .photo{position:absolute;left:0;top:0;width:533px;height:478px;background:linear-gradient(180deg,#c9b9a4 0%,#8a6d43 45%,#4a3424 75%,#6b2a22 100%)}
.feature h2{position:absolute;left:626px;top:74px;font-size:44px;font-weight:400;color:#3a3a3a;line-height:1}
.feature h3{position:absolute;left:626px;top:136px;font-size:34px;font-weight:400;color:#3a3a3a;letter-spacing:.5px;line-height:1}
.feature p{position:absolute;left:628px;top:201px;width:420px;font-family:var(--sans);font-size:13.5px;line-height:25.5px;color:#3a3a3a}
.feature .shop{position:absolute;left:628px;top:2228px;}
.feature-btn{left:628px;top:2228px;width:172px;height:53px;border:2px solid #4a4a4a;border-radius:27px;display:flex;align-items:center;justify-content:center;font-size:19px;color:#3a3a3a}

/* blog */
.post{width:313px;top:2520px}
.post .photo{width:313px;height:221px}
.post .date{margin-top:24px;font-size:16px;color:var(--ink)}
.post h4{margin-top:12px;font-size:21px;font-weight:400;color:var(--ink)}
.post p{margin-top:10px;font-family:var(--sans);font-size:13.5px;line-height:26px;color:var(--muted)}

/* newsletter */
.newsletter{left:0;top:2975px;width:1200px;height:396px;background:var(--mist)}
.newsletter .lead{position:absolute;left:0;top:126px;width:1200px;text-align:center;font-family:var(--sans);font-size:13.5px;line-height:26px;color:#555}
.email{left:243px;top:3172px;width:714px;height:60px;border:1px solid #cfcfcf;border-radius:30px;background:var(--white);padding-left:26px;display:flex;align-items:center;font-size:15px;color:#555}
.signup{left:510px;top:3255px;width:178px;height:58px;border-radius:29px;background:#3b3b3d;color:var(--white);font-size:17px;font-weight:600;display:flex;align-items:center;justify-content:center}

/* footer */
.footer{left:0;top:3371px;width:1200px;height:330px;background:var(--ink);color:var(--white);font-family:var(--round)}
.footer-brand{left:0;top:3488px;width:488px;text-align:center;font-family:var(--serif);font-size:21px;letter-spacing:4px;color:var(--white);font-weight:500}
.social{top:3554px;display:flex;gap:9px;left:140px}
.social span{width:34px;height:34px;border:1.5px solid var(--white);border-radius:50%}
.foot-head{top:3426px;font-size:20px;text-transform:uppercase}
.links{left:436px;top:3472px;list-style:none;font-size:12px;text-transform:uppercase}
.links li{height:30px;display:flex;align-items:center;gap:10px}
.contact{left:630px;font-size:14px;display:flex;align-items:center;gap:14px}
.contact .ico{width:30px;height:30px;border-radius:50%;background:#2a292b;display:flex;align-items:center;justify-content:center}
.pay-text{left:877px;top:3478px;width:220px;font-family:var(--sans);font-size:13px;line-height:24px}
.cards{left:877px;top:3542px;display:flex;gap:4px}
.cards span{width:39px;height:27px;background:#e6e6e6;border-radius:3px}
.bottombar{left:0;top:3701px;width:1200px;height:63px;background:var(--ink-deep);color:var(--white);font-family:var(--round);font-size:13.5px;display:flex;align-items:center;justify-content:center}
</style>
</head>
<body>

<div class="abs topbar">
  <div class="abs call">Call Us : 000-121-1231</div>
  <div class="abs account">
    <span>Sign in</span><span class="sep">|</span><span>Register</span><span class="sep">|</span>
    <span style="display:flex;align-items:center;gap:5px">
      <svg width="15" height="13" viewBox="0 0 15 13"><path d="M0 1h3l2 7h8l2-5H4" fill="none" stroke="#fff" stroke-width="1.6"/><circle cx="6" cy="11" r="1.3" fill="#fff"/><circle cx="12" cy="11" r="1.3" fill="#fff"/></svg>Cart (0)</span>
    <svg width="13" height="13" viewBox="0 0 13 13"><circle cx="5.5" cy="5.5" r="4" fill="none" stroke="#fff" stroke-width="2"/><path d="M8.5 8.5l3.5 3.5" stroke="#fff" stroke-width="2.2"/></svg>
  </div>
</div>

<div class="abs brand">LARKMOOR LANE</div>
<div class="abs header-rule"></div>
<div class="abs nav" style="left:215px">Home</div>
<div class="abs nav" style="left:358px">About Us</div>
<div class="abs nav" style="left:513px">Services</div>
<div class="abs nav" style="left:667px">Product</div>
<div class="abs nav" style="left:819px">Gallery</div>
<div class="abs nav" style="left:971px">Contact</div>

<div class="abs hero" role="img" aria-label="Dim still life of carved metal antiques, an ornate elephant figure and brass vessels on a patterned rug"></div>
<div class="abs hero-title">LARKMOOR LANE</div>
<div class="abs hero-sub">SED UT PERSPICIATIS UNDE OMNIS ISTE NATUS ERROR</div>
<div class="abs hero-btn">SHOP NOW</div>

<div class="abs section-title" style="top:975px">Our Products</div>
<div class="abs title-rule" style="top:1032px"></div>

<div class="abs product" style="left:112px;top:1067px"><div class="photo" role="img" aria-label="Brass singing bowls" style="background:linear-gradient(160deg,#7a5a2e,#c49a5a 50%,#3a2818)"></div><div class="price">$25.99</div><div class="name">Product Name</div><div class="details">View Details</div></div>
<div class="abs product" style="left:361px;top:1067px"><div class="photo" role="img" aria-label="Rows of carved wooden vases" style="background:linear-gradient(160deg,#3a2418,#8a4e30 50%,#2a1a12)"></div><div class="price">$25.99</div><div class="name">Product Name</div><div class="details">View Details</div></div>
<div class="abs product" style="left:609px;top:1067px"><div class="photo" role="img" aria-label="Antique upholstered carved chair" style="background:linear-gradient(160deg,#2a2622,#8a9088 50%,#4a3828)"></div><div class="price">$25.99</div><div class="name">Product Name</div><div class="details">View Details</div></div>
<div class="abs product" style="left:858px;top:1067px"><div class="photo" role="img" aria-label="Carved wooden figurines on painted boxes" style="background:linear-gradient(160deg,#9aa0a4,#b07a5a 50%,#6a2a22)"></div><div class="price">$25.99</div><div class="name">Product Name</div><div class="details">View Details</div></div>

<div class="abs product" style="left:112px;top:1479px"><div class="photo" role="img" aria-label="Painted enamel vases" style="background:linear-gradient(160deg,#2a1a10,#b0783a 50%,#3a2414)"></div><div class="price">$25.99</div><div class="name">Product Name</div><div class="details">View Details</div></div>
<div class="abs product" style="left:361px;top:1479px"><div class="photo" role="img" aria-label="Decorated metal pot" style="background:linear-gradient(160deg,#6a6a60,#a0886a 50%,#5a2a1a)"></div><div class="price">$25.99</div><div class="name">Product Name</div><div class="details">View Details</div></div>
<div class="abs product" style="left:609px;top:1479px"><div class="photo" role="img" aria-label="Gilded carved masks" style="background:linear-gradient(160deg,#1e1c1a,#8a6a2a 50%,#2a2420)"></div><div class="price">$25.99</div><div class="name">Product Name</div><div class="details">View Details</div></div>
<div class="abs product" style="left:858px;top:1479px"><div class="photo" role="img" aria-label="Engraved copper jugs" style="background:linear-gradient(160deg,#8a3a2a,#3a2a24 50%,#b0a8a0)"></div><div class="price">$25.99</div><div class="name">Product Name</div><div class="details">View Details</div></div>

<div class="abs feature">
  <div class="photo" role="img" aria-label="Ornate gilded crown resting on a stack of old leather-bound books"></div>
  <h2>Selling Antiques &amp;</h2>
  <h3>Unique Finds</h3>
  <p>Sed ut perspiciatis unde omnis iste natus error sit voluptatem acc usantium doloremque laudantium, totam rem aperiam, eaque ipsa quae ab illo inventore veritatis et quasi architecto beatae vitae dicta omnis iste natus sunt explicabo.</p>
</div>
<div class="abs feature-btn">Shop Now</div>

<div class="abs section-title" style="top:2428px">Latest Blog</div>
<div class="abs title-rule" style="top:2485px"></div>

<div class="abs post" style="left:111px"><div class="photo" role="img" aria-label="Jewelled antique crown" style="background:linear-gradient(170deg,#d8d2c8,#4a3a30 55%,#8a7a6a)"></div><div class="date">09 Feb 2021</div><h4>Sed ut perspiciatis unde iste</h4><p>Nemo enim ipsam voluptatem quia voluptas sit as pernatur aut odit aut fugit, sed quia consequuntur magni dolores eos qui ratione...</p></div>
<div class="abs post" style="left:443px"><div class="photo" role="img" aria-label="Gilded crown on old books" style="background:linear-gradient(170deg,#cfc4b4,#8a6a3a 50%,#3a2a1e)"></div><div class="date">09 Feb 2021</div><h4>Sed ut perspiciatis unde iste</h4><p>Nemo enim ipsam voluptatem quia voluptas sit as pernatur aut odit aut fugit, sed quia consequuntur magni dolores eos qui ratione...</p></div>
<div class="abs post" style="left:775px"><div class="photo" role="img" aria-label="Crown on a dark stand beneath a gilded frame" style="background:linear-gradient(170deg,#3a3024,#c8bcac 45%,#6a4a2e)"></div><div class="date">09 Feb 2021</div><h4>Sed ut perspiciatis unde iste</h4><p>Nemo enim ipsam voluptatem quia voluptas sit as pernatur aut odit aut fugit, sed quia consequuntur magni dolores eos qui ratione...</p></div>

<div class="abs newsletter">
  <div class="abs section-title" style="top:46px">Newsletter Sign Up</div>
  <div class="abs title-rule" style="top:106px"></div>
  <div class="lead">Sed ut perspiciatis unde omnis iste natus error sit voluptatem accusantium doloremque<br>laudantium totam rem aperiam, eaque ipsa quae</div>
</div>
<div class="abs email">Enter Your Email :</div>
<div class="abs signup">SIGN UP</div>

<div class="abs footer"></div>
<div class="abs footer-brand">LARKMOOR LANE</div>
<div class="abs social"><span></span><span></span><span></span><span></span><span></span></div>

<div class="abs foot-head" style="left:436px;color:#fff;font-family:var(--round)">Quick Links</div>
<ul class="abs links" style="color:#fff;font-family:var(--round)">
  <li><svg width="16" height="6" viewBox="0 0 16 6"><path d="M0 3h14M11 .5L14 3l-3 2.5" fill="none" stroke="#fff"/></svg>Home</li>
  <li><svg width="16" height="6" viewBox="0 0 16 6"><path d="M0 3h14M11 .5L14 3l-3 2.5" fill="none" stroke="#fff"/></svg>About Us</li>
  <li><svg width="16" height="6" viewBox="0 0 16 6"><path d="M0 3h14M11 .5L14 3l-3 2.5" fill="none" stroke="#fff"/></svg>Services</li>
  <li><svg width="16" height="6" viewBox="0 0 16 6"><path d="M0 3h14M11 .5L14 3l-3 2.5" fill="none" stroke="#fff"/></svg>Product</li>
  <li><svg width="16" height="6" viewBox="0 0 16 6"><path d="M0 3h14M11 .5L14 3l-3 2.5" fill="none" stroke="#fff"/></svg>Gallery</li>
  <li><svg width="16" height="6" viewBox="0 0 16 6"><path d="M0 3h14M11 .5L14 3l-3 2.5" fill="none" stroke="#fff"/></svg>Contact</li>
</ul>

<div class="abs foot-head" style="left:630px;color:#fff;font-family:var(--round)">Contact Us</div>
<div class="abs contact" style="top:3475px;color:#fff;font-family:var(--round)"><span class="ico"><svg width="12" height="12" viewBox="0 0 12 12"><path d="M2 1l2 0 1 3-1.5 1a7 7 0 003.5 3.5L8 7l3 1v2a1 1 0 01-1 1A9 9 0 011 2a1 1 0 011-1z" fill="#fff"/></svg></span>000-121-1231</div>
<div class="abs contact" style="top:3525px;color:#fff;font-family:var(--round)"><span class="ico"><svg width="12" height="10" viewBox="0 0 12 10"><rect x=".5" y=".5" width="11" height="9" fill="none" stroke="#fff"/><path d="M.5 .5L6 5l5.5-4.5" fill="none" stroke="#fff"/></svg></span>info@company.com</div>
<div class="abs contact" style="top:3578px;color:#fff;font-family:var(--round);align-items:flex-start;line-height:24px"><span class="ico"><svg width="9" height="12" viewBox="0 0 9 12"><path d="M4.5 12S0 6.8 0 4.5a4.5 4.5 0 019 0C9 6.8 4.5 12 4.5 12z" fill="#fff"/><circle cx="4.5" cy="4.5" r="1.6" fill="#2a292b"/></svg></span><span>2172 Lorem Ipsum<br>dummy text 32308</span></div>

<div class="abs foot-head" style="left:877px;color:#fff;font-family:var(--round)">Payments</div>
<div class="abs pay-text" style="color:#fff">Sed ut perspiciatis unde omnis us error sit voluptatem</div>
<div class="abs cards"><span></span><span></span><span></span><span></span><span></span></div>

<div class="abs bottombar">© Copyrights 2021-Larkmoor Lane.All Rights Reserved.</div>

</body>
</html>
```